Small Business Consulting Firm Needs Business Card Design

Need a sleek modern business card with 2 sides matching the colors of our logo. We will be placing these with a mailer we are sending out. These business cards will only ever be given to business owners. We operate helping businesses who are struggling with cash flow or finances. If the green and blue design needs to be moved to the right of "Brightpath Ledger Consulting" for aesthetic purposes that is ok. We will need an editable file if possible. We would like to include the reps name, email, website, and phone number. For now just use Owen Parrish, oparrish@brightpathledger.com, www.brightpathledger.com, and 855-219-7038.

```html
<!DOCTYPE html>
<html lang="en">
<head>
<meta charset="utf-8">
<title>Brightpath Ledger Consulting — Business Card</title>
<link href="https://fonts.googleapis.com/css2?family=Lato:wght@400;700&display=swap" rel="stylesheet">
<style>
  :root {
    --navy: #115b92;
    --green: #6fb63f;
    --blue-line: #3f7fb5;
    --ink: #2b2b2b;
    --paper: #ffffff;
    --backdrop: #d7d9dc;
  }
  * { box-sizing: border-box; margin: 0; padding: 0; }
  html, body { width: 1200px; height: 800px; overflow: hidden; }
  body {
    background: var(--backdrop);
    font-family: "Lato", sans-serif;
    display: flex;
    align-items: center;
    justify-content: center;
    gap: 40px;
  }
  .card {
    position: relative;
    width: 560px;
    height: 320px;
    overflow: hidden;
    box-shadow: 0 6px 18px rgba(0,0,0,0.18);
  }
  .card--front { background: var(--navy); }
  .card--back { background: var(--paper); }

  .wordmark { position: absolute; line-height: 1; }
  .wordmark__name {
    display: block;
    font-size: 22px;
    font-weight: 400;
    letter-spacing: 3px;
    text-transform: uppercase;
  }
  .wordmark__sub {
    display: block;
    margin-top: 4px;
    font-size: 9px;
    letter-spacing: 7px;
    text-transform: uppercase;
    padding-left: 34px;
  }
  .card--front .wordmark { left: 36px; top: 196px; color: #fff; }
  .card--front .mark-square {
    position: absolute;
    right: 44px;
    top: 70px;
    width: 170px;
    height: 170px;
    background: var(--green);
  }

  .card--back .wordmark { right: 92px; top: 60px; color: var(--ink); text-align: left; }
  .card--back .wordmark__name { font-size: 19px; }
  .card--back .wordmark__sub { font-size: 8px; padding-left: 30px; }
  .card--back .mark-square {
    position: absolute;
    right: 40px;
    top: 58px;
    width: 38px;
    height: 38px;
    background: var(--green);
  }

  .rep { position: absolute; left: 54px; top: 128px; }
  .rep__name { color: var(--green); font-size: 22px; font-weight: 700; }
  .rep__title { color: var(--ink); font-size: 15px; margin-top: 2px; }

  .rule { position: absolute; top: 184px; height: 1px; }
  .rule--green { left: 0; width: 40px; background: var(--green); }
  .rule--blue { left: 44px; right: 40px; background: var(--blue-line); }

  .contact { position: absolute; left: 36px; top: 200px; list-style: none; }
  .contact li {
    display: flex;
    align-items: center;
    gap: 8px;
    color: var(--ink);
    font-size: 15px;
    line-height: 22px;
  }
  .contact svg { width: 13px; height: 13px; fill: var(--navy); flex: none; }
</style>
</head>
<body>
  <section class="card card--front" aria-label="Card front">
    <div class="wordmark">
      <span class="wordmark__name">Brightpath Ledger</span>
      <span class="wordmark__sub">Consulting</span>
    </div>
    <div class="mark-square" aria-hidden="true"></div>
  </section>

  <section class="card card--back" aria-label="Card back">
    <div class="wordmark">
      <span class="wordmark__name">Brightpath Ledger</span>
      <span class="wordmark__sub">Consulting</span>
    </div>
    <div class="mark-square" aria-hidden="true"></div>

    <div class="rep">
      <p class="rep__name">Owen Parrish</p>
      <p class="rep__title">Representative</p>
    </div>
    <div class="rule rule--green"></div>
    <div class="rule rule--blue"></div>

    <ul class="contact">
      <li>
        <svg viewBox="0 0 24 24" aria-hidden="true"><path d="M6.6 10.8a15.1 15.1 0 0 0 6.6 6.6l2.2-2.2a1 1 0 0 1 1-.25 11.4 11.4 0 0 0 3.6.57 1 1 0 0 1 1 1V20a1 1 0 0 1-1 1A17 17 0 0 1 3 4a1 1 0 0 1 1-1h3.5a1 1 0 0 1 1 1c0 1.25.2 2.45.57 3.57a1 1 0 0 1-.25 1z"/></svg>
        855-219-7038
      </li>
      <li>
        <svg viewBox="0 0 24 24" aria-hidden="true"><path d="M2 5h20v14H2zm2 2v.4l8 5.2 8-5.2V7zm0 2.8V17h16V9.8l-8 5.2z"/></svg>
        oparrish@brightpathledger.com
      </li>
      <li>
        <svg viewBox="0 0 24 24" aria-hidden="true"><path d="M12 2a10 10 0 1 0 0 20 10 10 0 0 0 0-20zm6.9 6h-3a15 15 0 0 0-1.3-3.9A8 8 0 0 1 18.9 8zM12 4c.8 1.2 1.5 2.5 1.9 4h-3.8c.4-1.5 1.1-2.8 1.9-4zM4.3 14a8 8 0 0 1 0-4h3.4a16 16 0 0 0 0 4zm.8 2h3a15 15 0 0 0 1.3 3.9A8 8 0 0 1 5.1 16zm3-8h-3a8 8 0 0 1 4.3-3.9A15 15 0 0 0 8.1 8zM12 20c-.8-1.2-1.5-2.5-1.9-4h3.8c-.4 1.5-1.1 2.8-1.9 4zm2.3-6H9.7a14 14 0 0 1 0-4h4.6a14 14 0 0 1 0 4zm.3 5.9a15 15 0 0 0 1.3-3.9h3a8 8 0 0 1-4.3 3.9zm1.7-5.9a16 16 0 0 0 0-4h3.4a8 8 0 0 1 0 4z"/></svg>
        www.brightpathledger.com
      </li>
    </ul>
  </section>
</body>
</html>
```